Outdoor sign for Brindle Auto Restoration

I need a horizontal 4'x 8' outdoor roadside sign for my classic auto restoration business. I have uploaded colors and our logo. Needs the Brindle name, a prominent Classic AUTO RESTORATION, phone number and website. We rebuild and restore vintage cars, trucks and 4x4s. I'd like something clean but possibly retro. Classic Auto Restoration is more important than the Brindle name. It needs to be visible and readable from the street. NO CLIP ART

Target Market(s)

Customers who need their vintage care restored or upgraded. Men and women ages 25-75

Industry/Entity Type

Automotive

Colors
FFC000
F8CF3A
FAE287
FDF2CF
FEFAEE

Requirements
Must have
• Legible. Bright. Readable as a backlit 4' x 8' large horizontal sign (roughly 120cm X 240cm)
Nice to have
• Use of the Brindle logo/type, Complete or Classic before prominent AUTO RESTORATION
Should not have
• Clip art of old cars or icons. And we don't want the Brindle Logo from the website because it wont be legible from the road. I have included the Illustrator file for Brindle text in the uploads

```html
<!DOCTYPE html>
<html lang="en">
<head>
<meta charset="UTF-8">
<title>Brindle Auto Restoration – Roadside Sign</title>
<link rel="stylesheet" href="https://fonts.googleapis.com/css2?family=Anton&family=Pinyon+Script&family=Oswald:wght@700&family=Roboto+Condensed:wght@700&display=swap">
<style>
  :root {
    --sign-black: #231f20;
    --sign-gold: #f8ae18;
    --sign-white: #ffffff;
  }
  html, body {
    margin: 0;
    padding: 0;
    width: 1200px;
    height: 600px;
    overflow: hidden;
    background: var(--sign-black);
  }
  .sign {
    display: block;
    width: 1200px;
    height: 600px;
  }
  .sign__background { fill: var(--sign-black); }
  .sign__band { fill: var(--sign-gold); }
  .sign__eyebrow {
    font-family: "Pinyon Script", cursive;
    font-size: 116px;
    fill: var(--sign-gold);
  }
  .sign__headline {
    font-family: "Anton", sans-serif;
    font-size: 200px;
    fill: var(--sign-black);
  }
  .sign__phone {
    font-family: "Roboto Condensed", sans-serif;
    font-weight: 700;
    font-size: 72px;
    fill: var(--sign-white);
  }
  .sign__brand {
    font-family: "Oswald", sans-serif;
    font-weight: 700;
    font-size: 92px;
    fill: var(--sign-gold);
  }
  .sign__website {
    font-family: "Roboto Condensed", sans-serif;
    font-weight: 700;
    font-size: 38px;
    fill: var(--sign-white);
  }
</style>
</head>
<body>
<svg class="sign" viewBox="0 0 1200 600" xmlns="http://www.w3.org/2000/svg" role="img" aria-label="Brindle Classic Auto Restoration sign">
  <rect class="sign__background" x="0" y="0" width="1200" height="600"/>
  <path class="sign__band" d="M0,166 Q600,228 1200,166 L1200,488 Q600,428 0,488 Z"/>

  <text class="sign__eyebrow" x="601" y="136" text-anchor="middle">Classic</text>

  <text class="sign__headline" x="38" y="414" textLength="1125" lengthAdjust="spacingAndGlyphs">AUTO RESTORATION</text>

  <text class="sign__phone" x="38" y="553" textLength="300" lengthAdjust="spacingAndGlyphs">501-555-0142</text>
  <text class="sign__brand" x="602" y="561" text-anchor="middle" textLength="416" lengthAdjust="spacingAndGlyphs">BRINDLE</text>
  <text class="sign__website" x="1163" y="541" text-anchor="end" textLength="302" lengthAdjust="spacingAndGlyphs">brindleautoworks.com</text>
</svg>
</body>
</html>
```